Dental Design, very professional and noticable

Tindale Ridge Dental Surgery is based in Pelican Waters. We are a fast growing dental surgery and are looking for some professional business cards to send to patients.
We would like to see a design that is Vertical and uses the colours Soft Blue, Silver, White and Black. Maybe a full blue side with moto and details on back? Any other ideas or colours that you may think will make the card look unique is fine.
We need all details on the card that are listed above

Target Market(s)

Families, Retired, Other Professionals and Businesses

Industry/Entity Type

Dental

Contact Information for Business Card

Tindale Ridge Dental Surgery
Family, Cosmetic, Preventative
Dr. Owen Castrey
Dental Surgeon
BDS (Adel) FAE FADI FICD FPFA
phone: (07)50001846
fax: (07)50002917
email: tindaleridgedental@quillpost.com
http://tindaleridgedental.com/

Logo Text

Logo styles of interest
Abstract Logo
Requirements
Must have
• Vertical, Vibrant but Professional, Rounded Edges, Logo on front and back of card (different colours on each side)
Nice to have
• One side completely blue (not sure what shade) with logo and moto on bottom
Other side white, with blue or different coloured logo with details in black and silver?
Logo should show half circle with 1 end as arrow symbolizing pelican waters canal also a magnifine glass also half circled with 1 end as arrow. Any other ideas are welcome.
Should not have
• A tooth. A smile. Toothbrush or Toothpaste. Cornered edges.

```html
<!DOCTYPE html>
<html lang="en">
<head>
<meta charset="utf-8">
<title>Tindale Ridge Dental Surgery – Business Card</title>
<link rel="stylesheet" href="https://fonts.googleapis.com/css2?family=Cormorant+Garamond:wght@500&family=Open+Sans:wght@400;600&family=Fira+Sans+Condensed:wght@500&family=Josefin+Sans:wght@400&display=swap">
<style>
  :root {
    --stage: #3b3b3d;
    --blue-deep: #0d5cb0;
    --blue-light: #3f8fd6;
    --sky: #27b5ea;
    --band: #00bdf2;
    --white: #ffffff;
    --gold: #8c6d2c;
    --gold-bright: #b8951f;
    --grey: #8e8e8e;
    --faint: #efeae0;
  }
  * { margin: 0; padding: 0; box-sizing: border-box; }
  html, body {
    width: 1200px; height: 1000px; overflow: hidden;
    background: var(--stage);
  }
  .canvas { position: relative; width: 1200px; height: 1000px; }

  .card {
    position: absolute; top: 146px;
    width: 400px; height: 708px;
    border-radius: 24px; overflow: hidden;
  }

  /* Front */
  .card-front {
    left: 170px;
    background: radial-gradient(ellipse 260px 380px at 50% 45%, var(--blue-light) 0%, var(--blue-deep) 100%);
  }
  .front-mark {
    position: absolute; left: 160px; top: 230px;
    width: 80px; height: 80px; border-radius: 50%;
    background: var(--sky);
  }
  .front-name {
    position: absolute; left: 0; right: 0; top: 372px;
    text-align: center;
    font-family: "Cormorant Garamond", serif; font-weight: 500;
    font-size: 30px; line-height: 36px; letter-spacing: -0.3px;
    color: var(--sky);
  }
  .front-band {
    position: absolute; left: 0; right: 0; top: 420px; height: 26px;
    background: var(--band);
    text-align: center;
    font-family: "Open Sans", sans-serif;
    font-size: 17px; line-height: 26px;
    color: var(--white);
  }

  /* Back */
  .card-back { left: 630px; background: var(--white); }
  .back-decor {
    position: absolute; left: 200px; top: 500px;
    width: 300px; height: 300px; border-radius: 50%;
    background: var(--faint);
  }
  .back-mark {
    position: absolute; left: 167px; top: 70px;
    width: 66px; height: 66px; border-radius: 50%;
    background: var(--gold);
  }
  .back-name {
    position: absolute; left: 0; right: 0; top: 150px;
    text-align: center;
    font-family: "Fira Sans Condensed", sans-serif; font-weight: 500;
    font-size: 22px; color: var(--gold);
  }
  .back-tagline {
    position: absolute; left: 0; right: 0; top: 186px;
    text-align: center;
    font-family: "Fira Sans Condensed", sans-serif; font-weight: 500;
    font-size: 16px; color: var(--gold-bright);
  }
  .doctor {
    position: absolute; left: 48px; top: 300px;
    font-family: "Josefin Sans", sans-serif;
  }
  .doctor-name { font-size: 21px; color: #7d6a3a; }
  .doctor-role { font-size: 12px; color: var(--grey); margin-left: 4px; }
  .doctor-quals {
    display: block; margin-top: 1px;
    font-family: "Open Sans", sans-serif; font-weight: 600;
    font-size: 8.5px; color: var(--gold-bright);
  }
  .contact {
    position: absolute; left: 48px; top: 354px; list-style: none;
    font-family: "Open Sans", sans-serif; font-size: 12px; color: var(--gold-bright);
  }
  .contact li { display: flex; align-items: center; height: 21px; white-space: nowrap; }
  .contact svg { width: 20px; height: 16px; margin-right: 10px; fill: none; stroke: var(--gold); stroke-width: 1.6; flex: none; }
  .contact .solid { fill: var(--gold); stroke: none; }
</style>
</head>
<body>
<main class="canvas">

  <section class="card card-front" aria-label="Card front">
    <div class="front-mark"></div>
    <h1 class="front-name">Tindale Ridge Dental Surgery</h1>
    <p class="front-band">Family, Cosmetic, Preventive</p>
  </section>

  <section class="card card-back" aria-label="Card back">
    <div class="back-decor"></div>
    <div class="back-mark"></div>
    <h2 class="back-name">Tindale Ridge Dental Surgery</h2>
    <p class="back-tagline">Family, Cosmetic, Preventive</p>

    <div class="doctor">
      <span class="doctor-name">Dr. Owen Castrey</span><span class="doctor-role">Dental Surgeon</span>
      <span class="doctor-quals">BDS (Adel) FAE FADI FICD FPFA</span>
    </div>

    <ul class="contact">
      <li>
        <svg viewBox="0 0 20 16"><path class="solid" d="M2 4 Q10 -1 18 4 L16 7 L13 6 L13 4 Q10 3 7 4 L7 6 L4 7 Z"/><rect class="solid" x="4" y="8" width="12" height="7" rx="1"/></svg>
        phone: (07)50001846
      </li>
      <li>
        <svg viewBox="0 0 20 16"><rect x="6" y="1" width="8" height="5"/><rect x="3" y="6" width="14" height="6"/><rect x="6" y="10" width="8" height="5"/></svg>
        fax: (07)50002917
      </li>
      <li>
        <svg viewBox="0 0 20 16"><rect class="solid" x="1" y="3" width="18" height="11"/><path d="M1 3 L10 10 L19 3" stroke="#fff"/></svg>
        email: tindaleridgedental@quillpost.com
      </li>
      <li>
        <svg viewBox="0 0 20 16"><circle cx="10" cy="8" r="7"/><ellipse cx="10" cy="8" rx="3" ry="7"/><path d="M3 8 H17 M4.5 4.5 H15.5 M4.5 11.5 H15.5"/></svg>
        http://tindaleridgedental.com/
      </li>
    </ul>
  </section>

</main>
</body>
</html>
```